Pregnancy and Fertility Information Website

Hello Designers,
I need a website which provide tips and information about healthy and happy pregnancy. My website name is KRE medical.

The website should provide all the information needed throughout pregnancy and beyond ranging from pregnancy tracking tools and articles about common pregnancy concerns and what to expect during pregnancy,etc.
The details about first trimester, second trimester and third trimester should be highlighted in the website.

Top Navigation
Home, Fertility, Pregnancy basics, Articles, Tips and News

I'm looking for a simple and clean design which involves captivating images and colors but it shouldn't be crowded. The design must be professional and modern. An easy to navigate layout is a must.

Green, violet, blue and light yellow colors are my favorites but i'm open to other options.

Any questions. Kindly ask

Industry/Entity Type

Medical

```html
<!DOCTYPE html>
<html lang="en">
<head>
<meta charset="utf-8">
<title>KRE Medical – Healthy and Happy Pregnancy</title>
<link rel="stylesheet" href="https://fonts.googleapis.com/css2?family=Lato:wght@700;900&family=Open+Sans:wght@400;600&family=Vollkorn:wght@400;500&family=Vollkorn+SC:wght@400;600&family=Courgette&display=swap">
<style>
:root{
  --green:#22a652;
  --green-dark:#178a41;
  --blue:#1b5ea8;
  --blue-dark:#124a88;
  --pink:#e8567b;
  --ink:#333;
  --text:#6a6a6a;
  --muted:#999;
  --panel:#ebebeb;
  --panel-light:#f5f5f5;
  --white:#fff;
}
*{box-sizing:border-box;margin:0;padding:0}
html,body{width:1200px;height:3455px;overflow:hidden}
body{position:relative;background:var(--white);font-family:"Open Sans",sans-serif;color:var(--text)}
.abs{position:absolute}
.title{font-family:"Vollkorn",serif;font-weight:400;letter-spacing:1px;font-size:40px;line-height:1}
.lead{font-size:15.5px;line-height:25px;color:var(--text);text-align:center}
.btn{position:absolute;display:flex;align-items:center;justify-content:center;border-radius:26px;color:var(--white);font-size:17px;font-weight:600;border:3px solid var(--white);box-shadow:0 0 0 2px currentColor}
.btn-green{background:var(--green);box-shadow:0 0 0 2px var(--green)}
.btn-blue{background:var(--blue);box-shadow:0 0 0 2px var(--blue)}
.btn span{margin-left:8px;font-size:15px}

/* header */
.topline{top:0;left:0;width:1200px;height:4px;background:var(--green)}
.nav{top:0;left:0;width:1200px;height:120px}
.nav a{position:absolute;top:48px;font-family:"Vollkorn",serif;font-size:19px;color:#222;text-decoration:none;letter-spacing:.5px}
.brand{position:absolute;left:540px;top:16px;width:120px;height:96px;display:flex;flex-direction:column;align-items:center;justify-content:center}
.brand-dot{width:46px;height:46px;border-radius:50%;background:var(--green);opacity:.85}
.brand-name{font-family:"Vollkorn",serif;font-size:18px;color:var(--blue);margin-top:4px;letter-spacing:1px}

/* hero */
.hero-photo{top:0;left:0;width:1200px;height:690px;background:linear-gradient(100deg,#f6f6f4 0%,#eeeeec 45%,#dfe3ea 62%,#c9d5e6 75%,#eceae8 100%)}
.hero-name{left:80px;top:255px;font-family:"Lato",sans-serif;font-weight:900;font-size:52px;color:var(--blue);letter-spacing:1px}
.hero-tag{left:80px;top:322px;font-family:"Courgette",cursive;font-size:26px;line-height:38px;color:#222}
.hero-btn{left:80px;top:419px;width:203px;height:53px}

/* welcome */
.welcome-title{top:762px;left:0;width:1200px;text-align:center;color:var(--green)}
.welcome-text{top:823px;left:125px;width:950px}
.welcome-btn{left:514px;top:956px;width:172px;height:51px}

/* fertility / pregnancy */
.panel-left{top:1060px;left:0;width:600px;height:426px;background:var(--panel)}
.panel-right{top:1060px;left:600px;width:600px;height:426px;background:var(--panel-light)}
.feature-title{top:1115px}
.feature-photo{width:232px;height:232px;border-radius:50%;border:4px solid var(--white)}
.feature-badge{width:84px;height:84px;border-radius:50%;border:4px solid var(--white);display:flex;align-items:center;justify-content:center}
.feature-text{width:240px;font-size:15.5px;line-height:25px}
.feature-btn{width:174px;height:52px}

/* trimester */
.tri-title{top:1540px;left:0;width:1200px;text-align:center;color:var(--green);letter-spacing:2px}
.tri-text{top:1600px;left:120px;width:960px}
.tri-art{top:1693px;left:370px;width:770px;height:276px;background:linear-gradient(180deg,#c5d3e6 0%,#d7e1ee 60%,rgba(255,255,255,0) 100%);border-radius:8px}
.tri-card{top:1681px;left:94px;width:252px;height:276px;background:var(--white);border:2px solid #bfe2c9;border-radius:18px;padding:20px 22px}
.tri-card h3{font-family:"Vollkorn SC",serif;font-weight:600;font-size:22px;color:var(--blue);margin-bottom:10px}
.tri-card p{font-size:15.5px;line-height:25px}
.tri-card a{color:var(--blue);text-decoration:underline}
.tri-pointer{top:1950px;left:152px}
.timeline{top:2024px;left:0;width:1200px;height:2px;background:#e3e3e3}
.marker{position:absolute;top:1999px;width:50px;height:48px}
.units{top:2050px;left:1010px;font-size:14px;color:#666}
.stage{position:absolute;top:2085px;width:260px;text-align:center}
.stage h4{font-family:"Vollkorn SC",serif;font-weight:500;font-size:22px}
.stage .rule{height:2px;margin:12px 30px 14px;position:relative}
.stage .rule::before,.stage .rule::after{content:"";position:absolute;top:-3px;width:8px;height:8px;border-radius:50%;background:inherit}
.stage .rule::before{left:0}.stage .rule::after{right:0}
.stage p{font-family:"Vollkorn SC",serif;font-size:22px;color:#333}

/* articles */
.art-left{top:2229px;left:0;width:600px;height:431px;background:var(--panel-light)}
.art-right{top:2229px;left:600px;width:600px;height:431px;background:var(--panel)}
.list-title{top:2286px}
.post{position:absolute;width:520px;height:110px}
.post-img{position:absolute;left:0;top:0;width:158px;height:104px}
.post-body{position:absolute;left:184px;top:0;width:336px;font-size:15.5px;line-height:24px}
.post-body h5{font-weight:400;font-size:15.5px}
.post-date{color:#555}
.post-body a{text-decoration:underline}
.divider{position:absolute;height:1px;background:#c8c8c8;width:470px}

/* testimonials */
.testi-title{top:2688px;left:0;width:1200px;text-align:center;color:var(--blue-dark);letter-spacing:2px}
.testi-card{top:2770px;left:182px;width:845px;height:173px;background:#efefef;border-bottom:3px solid var(--blue);box-shadow:0 10px 14px rgba(0,0,0,.12)}
.testi-card p{position:absolute;top:40px;left:110px;width:625px;text-align:center;font-size:14.5px;line-height:28px}
.testi-client{position:absolute;top:118px;left:0;width:100%;text-align:center;font-family:"Vollkorn SC",serif;color:var(--blue);font-size:15px}
.quote{position:absolute;font-family:"Vollkorn",serif;font-size:140px;color:#d9d9d9;line-height:1}
.dots{top:2965px;left:574px;display:flex;gap:12px}
.dots i{width:12px;height:12px;border-radius:50%;background:#ccc}
.dots i.on{background:var(--green)}

/* footer */
.footer-photo{top:3017px;left:0;width:1200px;height:387px;background:linear-gradient(180deg,#f1ede9 0%,#f7f4f2 50%,#fbfaf9 100%)}
.footer-brand{top:3070px;left:560px;width:80px;height:72px;display:flex;flex-direction:column;align-items:center}
.footer-brand .brand-dot{width:36px;height:36px;background:#8a8a8a}
.footer-brand .brand-name{font-size:15px;color:#555}
.foot-h{font-family:"Vollkorn SC",serif;font-size:19px;color:var(--blue);letter-spacing:1px}
.foot-list{list-style:none;font-size:15px;color:#333;line-height:38px}
.about{top:3190px;left:78px;width:200px;font-size:15.5px;line-height:25px;color:#333}
.social{position:absolute;top:3295px;width:50px;height:50px;border-radius:50%;background:var(--white);box-shadow:0 2px 6px rgba(0,0,0,.12)}
.social.main{background:var(--blue)}
.field{position:absolute;left:622px;width:234px;height:42px;border:1px solid #555;background:var(--white);font-size:14px;color:#333;padding:11px 8px}
.subscribe{position:absolute;top:3330px;left:620px;width:138px;height:42px;background:var(--blue);color:var(--white);font-family:"Vollkorn",serif;font-size:17px;display:flex;align-items:center;justify-content:center}
.contact{position:absolute;left:891px;font-size:15px;color:#333;line-height:23px;display:flex;gap:10px}
.contact svg{flex:none;margin-top:3px}
.copy{top:3404px;left:0;width:1200px;height:51px;background:var(--green);color:var(--white);font-size:14px;display:flex;align-items:center;justify-content:center}
</style>
</head>
<body>

<!-- Hero -->
<div class="abs hero-photo" role="img" aria-label="Photo of a smiling pregnant woman in a light blue shirt sitting cross-legged against a white brick wall"></div>
<div class="abs topline"></div>
<nav class="abs nav">
  <a style="left:80px">HOME</a>
  <a style="left:177px">FERTILITY</a>
  <a style="left:310px">PREGNANCY BASICS</a>
  <div class="brand"><div class="brand-dot"></div><div class="brand-name">KRE</div></div>
  <a style="left:731px">ARTICLES</a>
  <a style="left:888px">TIPS AND NEWS</a>
  <svg class="abs" style="left:1100px;top:52px" width="22" height="22" viewBox="0 0 22 22"><circle cx="9" cy="9" r="7" fill="none" stroke="#222" stroke-width="2.6"/><line x1="14" y1="14" x2="20" y2="20" stroke="#222" stroke-width="3" stroke-linecap="round"/></svg>
</nav>
<h1 class="abs hero-name">KRE MEDICAL</h1>
<p class="abs hero-tag">We provide tips and information about<br>healthy and happy pregnancy</p>
<div class="btn btn-green hero-btn">CONTACT US NOW</div>
<svg class="abs" style="left:0;top:520px" width="1200" height="190" viewBox="0 0 1200 190">
  <path d="M0 20 C250 170 800 190 1200 50 L1200 190 L0 190 Z" fill="#f7f7f7"/>
  <path d="M0 20 C250 170 800 190 1200 50" fill="none" stroke="var(--blue)" stroke-width="5"/>
  <path d="M500 168 C800 180 1000 120 1200 56" fill="none" stroke="var(--green)" stroke-width="6"/>
</svg>

<!-- Welcome -->
<div class="abs" style="top:690px;left:0;width:1200px;height:370px;background:#f7f7f7"></div>
<h2 class="abs title welcome-title">WELCOME TO KRE MEDICAL</h2>
<p class="abs lead welcome-text">Lorem Ipsum is simply dummy text of the printing and typesetting industry. Lorem Ipsum has been the industry's standard dummy text ever since the 1500s, when an unknown printer took a galley of type and scrambled it to make a type specimen book. It has survived not only five centuries, but also the leap into electronic typesetting, remaining essentially unchanged. It was popularised in the 1960s with the release of Letraset sheets containing Lorem Ipsum passages...</p>
<div class="btn btn-green welcome-btn">READ MORE <span>»</span></div>

<!-- Fertility / Pregnancy basics -->
<div class="abs panel-left"></div>
<div class="abs panel-right"></div>
<h2 class="abs title feature-title" style="left:80px;color:var(--blue)">FERTILITY</h2>
<h2 class="abs title feature-title" style="left:644px;color:var(--green)">PREGNANCY BASICS</h2>

<div class="abs feature-photo" style="left:80px;top:1202px;background:linear-gradient(150deg,#eee 0%,#d8d8d8 60%,#f0c8d6 100%);box-shadow:0 0 0 3px var(--blue)" role="img" aria-label="Photo of a pregnant belly holding a pink flower bouquet"></div>
<div class="abs feature-badge" style="left:214px;top:1196px;background:var(--blue)">
  <svg width="40" height="40" viewBox="0 0 40 40" fill="none" stroke="#fff" stroke-width="3"><rect x="8" y="6" width="24" height="28" rx="3"/><circle cx="20" cy="16" r="4"/><path d="M13 30c0-6 3-9 7-9s7 3 7 9"/></svg>
</div>
<p class="abs feature-text" style="left:330px;top:1198px">Lorem Ipsum is simply dummy text of the printing and typesetting industry. Lorem Ipsum has been the industry's standard dummy text ever since the 1500s, when an unknown...</p>
<div class="btn btn-blue feature-btn" style="left:330px;top:1379px">READ MORE <span>»</span></div>

<div class="abs feature-photo" style="left:642px;top:1202px;background:linear-gradient(150deg,#cfd8b8 0%,#b79f88 55%,#e9e2d6 100%);box-shadow:0 0 0 3px var(--green)" role="img" aria-label="Photo of an expecting couple outdoors"></div>
<div class="abs feature-badge" style="left:776px;top:1196px;background:var(--green)">
  <svg width="40" height="40" viewBox="0 0 40 40" fill="none" stroke="#fff" stroke-width="3"><circle cx="20" cy="9" r="4"/><path d="M16 16c-2 6-1 12 2 18M18 22c6-2 10 2 9 6s-6 5-9 3"/></svg>
</div>
<p class="abs feature-text" style="left:892px;top:1198px">Lorem Ipsum is simply dummy text of the printing and typesetting industry. Lorem Ipsum has been the industry's standard dummy text ever since the 1500s, when an unknown...</p>
<div class="btn btn-green feature-btn" style="left:892px;top:1379px">READ MORE <span>»</span></div>

<!-- Trimester chart -->
<h2 class="abs title tri-title">TRIMESTER &nbsp;CHART</h2>
<p class="abs lead tri-text">Lorem Ipsum is simply dummy text of the printing and typesetting industry. Lorem Ipsum has been the industry's standard dummy text ever since the 1500s, when an unknown printer took a galley of type and scrambled.</p>
<div class="abs tri-art" role="img" aria-label="Row of pale blue pregnant silhouettes showing the baby growing week by week"></div>
<div class="abs tri-card">
  <h3>1st Trimester</h3>
  <p>Lorem Ipsum is simply dummy text of the printing and typesetting industry. Lorem Ipsum has been the industry's standard dummy text ever since the 1500s, when an unknown...<br><a>READ MORE</a></p>
</div>
<svg class="abs tri-pointer" width="26" height="16" viewBox="0 0 26 16"><path d="M0 0 L13 14 L26 0" fill="#fff" stroke="#bfe2c9" stroke-width="2"/></svg>

<div class="abs timeline"></div>
<svg class="marker" style="left:79px;top:1990px" width="50" height="66" viewBox="0 0 50 66"><circle cx="25" cy="33" r="24" fill="#fff" stroke="var(--blue)" stroke-width="3"/><text x="25" y="40" text-anchor="middle" font-family="Vollkorn,serif" font-size="20" fill="#222">4</text></svg>
<svg class="marker" style="left:189px" viewBox="0 0 50 48"><path d="M25 46 C8 34 2 24 2 15 C2 7 8 2 14 2 C19 2 23 5 25 9 C27 5 31 2 36 2 C42 2 48 7 48 15 C48 24 42 34 25 46Z" fill="var(--green)"/><text x="25" y="27" text-anchor="middle" font-family="Open Sans,sans-serif" font-size="14" fill="#fff">9</text></svg>
<svg class="marker" style="left:313px" viewBox="0 0 50 48"><path d="M25 46 C8 34 2 24 2 15 C2 7 8 2 14 2 C19 2 23 5 25 9 C27 5 31 2 36 2 C42 2 48 7 48 15 C48 24 42 34 25 46Z" fill="var(--pink)"/><text x="25" y="27" text-anchor="middle" font-family="Open Sans,sans-serif" font-size="14" fill="#fff">13</text></svg>
<svg class="marker" style="left:431px" viewBox="0 0 50 48"><path d="M25 46 C8 34 2 24 2 15 C2 7 8 2 14 2 C19 2 23 5 25 9 C27 5 31 2 36 2 C42 2 48 7 48 15 C48 24 42 34 25 46Z" fill="var(--pink)"/><text x="25" y="27" text-anchor="middle" font-family="Open Sans,sans-serif" font-size="14" fill="#fff">18</text></svg>
<svg class="marker" style="left:551px" viewBox="0 0 50 48"><path d="M25 46 C8 34 2 24 2 15 C2 7 8 2 14 2 C19 2 23 5 25 9 C27 5 31 2 36 2 C42 2 48 7 48 15 C48 24 42 34 25 46Z" fill="var(--pink)"/><text x="25" y="27" text-anchor="middle" font-family="Open Sans,sans-serif" font-size="14" fill="#fff">22</text></svg>
<svg class="marker" style="left:666px" viewBox="0 0 50 48"><path d="M25 46 C8 34 2 24 2 15 C2 7 8 2 14 2 C19 2 23 5 25 9 C27 5 31 2 36 2 C42 2 48 7 48 15 C48 24 42 34 25 46Z" fill="var(--pink)"/><text x="25" y="27" text-anchor="middle" font-family="Open Sans,sans-serif" font-size="14" fill="#fff">27</text></svg>
<svg class="marker" style="left:786px" viewBox="0 0 50 48"><path d="M25 46 C8 34 2 24 2 15 C2 7 8 2 14 2 C19 2 23 5 25 9 C27 5 31 2 36 2 C42 2 48 7 48 15 C48 24 42 34 25 46Z" fill="var(--pink)"/><text x="25" y="27" text-anchor="middle" font-family="Open Sans,sans-serif" font-size="14" fill="#fff">31</text></svg>
<svg class="marker" style="left:905px" viewBox="0 0 50 48"><path d="M25 46 C8 34 2 24 2 15 C2 7 8 2 14 2 C19 2 23 5 25 9 C27 5 31 2 36 2 C42 2 48 7 48 15 C48 24 42 34 25 46Z" fill="var(--pink)"/><text x="25" y="27" text-anchor="middle" font-family="Open Sans,sans-serif" font-size="14" fill="#fff">36</text></svg>
<svg class="marker" style="left:1025px" viewBox="0 0 50 48"><path d="M25 46 C8 34 2 24 2 15 C2 7 8 2 14 2 C19 2 23 5 25 9 C27 5 31 2 36 2 C42 2 48 7 48 15 C48 24 42 34 25 46Z" fill="var(--pink)"/><text x="25" y="27" text-anchor="middle" font-family="Open Sans,sans-serif" font-size="14" fill="#fff">40</text></svg>
<p class="abs units">*units in weeks</p>

<div class="stage" style="left:89px"><h4 style="color:var(--green-dark)">1st Trimester</h4><div class="rule" style="background:var(--green)"></div><p>0.4kg - 2.0kg</p></div>
<div class="stage" style="left:469px"><h4 style="color:var(--blue)">2nd Trimester</h4><div class="rule" style="background:var(--blue)"></div><p>2.0kg - 8.0kg</p></div>
<div class="stage" style="left:798px"><h4 style="color:var(--pink)">3rd Trimester</h4><div class="rule" style="background:var(--pink)"></div><p>8.0kg - 13.6kg</p></div>

<!-- Articles / Tips -->
<div class="abs art-left"></div>
<div class="abs art-right"></div>
<h2 class="abs title list-title" style="left:80px;color:var(--blue)">ARTICLES</h2>
<h2 class="abs title list-title" style="left:636px;color:var(--green)">TIPS AND NEWS</h2>

<div class="post" style="left:76px;top:2367px">
  <div class="post-img" style="background:linear-gradient(135deg,#7cc6d8,#3f8fb0)" role="img" aria-label="Photo of two pregnant women in teal"></div>
  <div class="post-body"><h5 style="color:var(--blue)">Lorem Ipsum is simply dummy text of</h5><div class="post-date">▦ February 13, 2017</div><div>Lorem Ipsum is simply dummy text of the printing and typesetting.... <a style="color:var(--blue)">READ MORE</a></div></div>
</div>
<div class="divider" style="left:76px;top:2487px"></div>
<div class="post" style="left:76px;top:2506px">
  <div class="post-img" style="background:linear-gradient(135deg,#f0d3da,#9fd0dc)" role="img" aria-label="Illustration of a pregnant belly with a tree drawing"></div>
  <div class="post-body"><h5 style="color:var(--blue)">Lorem Ipsum is simply dummy text of</h5><div class="post-date">▦ February 13, 2017</div><div>Lorem Ipsum is simply dummy text of the printing and typesetting.... <a style="color:var(--blue)">READ MORE</a></div></div>
</div>

<div class="post" style="left:636px;top:2367px">
  <div class="post-img" style="background:linear-gradient(135deg,#a6c56a,#5e8a3a)" role="img" aria-label="Photo of a pregnant woman standing in a green field"></div>
  <div class="post-body"><h5 style="color:var(--green)">Lorem Ipsum is simply dummy text of</h5><div class="post-date">▦ February 13, 2017</div><div>Lorem Ipsum is simply dummy text of the printing and typesetting.... <a style="color:var(--green)">READ MORE</a></div></div>
</div>
<div class="divider" style="left:650px;top:2487px"></div>
<div class="post" style="left:636px;top:2506px">
  <div class="post-img" style="background:linear-gradient(135deg,#d8b49c,#7a5a4a)" role="img" aria-label="Photo of hands forming a heart over a pregnant belly"></div>
  <div class="post-body"><h5 style="color:var(--green)">Lorem Ipsum is simply dummy text of</h5><div class="post-date">▦ February 13, 2017</div><div>Lorem Ipsum is simply dummy text of the printing and typesetting.... <a style="color:var(--green)">READ MORE</a></div></div>
</div>

<!-- Testimonials -->
<h2 class="abs title testi-title">TESTIMONIALS</h2>
<svg class="abs" style="left:578px;top:2752px" width="44" height="20" viewBox="0 0 44 20"><path d="M0 20 L22 0 L44 20Z" fill="#efefef"/></svg>
<div class="abs testi-card">
  <span class="quote" style="left:14px;top:-6px">“</span>
  <span class="quote" style="right:14px;top:52px">”</span>
  <p>Lorem Ipsum is simply dummy text of the printing and typesetting industry. Lorem Ipsum has been the industry's standard dummy text ever since the 1500s.</p>
  <div class="testi-client">— &nbsp;Client Name</div>
</div>
<div class="abs dots"><i></i><i class="on"></i><i></i></div>

<!-- Footer -->
<div class="abs footer-photo" role="img" aria-label="Faded photo of hands cradling a pregnant belly"></div>
<svg class="abs" style="left:0;top:3000px" width="1200" height="110" viewBox="0 0 1200 110">
  <path d="M0 0 L1200 0 L1200 100 C900 20 300 20 0 100 Z" fill="#fff"/>
  <path d="M0 100 C300 20 700 14 900 36" fill="none" stroke="var(--green)" stroke-width="6"/>
  <path d="M700 30 C900 40 1050 60 1200 100" fill="none" stroke="var(--blue)" stroke-width="6"/>
</svg>
<div class="abs footer-brand"><div class="brand-dot"></div><div class="brand-name">KRE</div></div>

<p class="abs about">We provide tips and information about healthy and happy pregnancy.</p>
<span class="social main" style="left:78px" aria-label="Social link"></span>
<span class="social" style="left:152px" aria-label="Social link"></span>
<span class="social" style="left:226px" aria-label="Social link"></span>

<h6 class="abs foot-h" style="left:350px;top:3156px">Useful Links</h6>
<ul class="abs foot-list" style="left:350px;top:3190px">
  <li>Home</li><li>Fertility</li><li>Pregnancy Basics</li><li>Articles</li><li>Tips And News</li>
</ul>

<h6 class="abs foot-h" style="left:622px;top:3156px">Newsletter</h6>
<div class="field" style="top:3204px">Enter Name</div>
<div class="field" style="top:3266px">Enter Email</div>
<div class="subscribe">SUBSCRIBE</div>

<h6 class="abs foot-h" style="left:891px;top:3156px">Contact Us</h6>
<div class="contact" style="top:3196px"><svg width="16" height="20" viewBox="0 0 16 20"><path d="M8 0a7 7 0 0 0-7 7c0 5 7 13 7 13s7-8 7-13a7 7 0 0 0-7-7z" fill="var(--blue)"/><circle cx="8" cy="7" r="2.6" fill="#fff"/></svg><span>123 Building name, Street<br>Name Country.</span></div>
<div class="contact" style="top:3267px;font-weight:600"><svg width="16" height="16" viewBox="0 0 16 16"><path d="M3 1l3 3-2 2c1 2 3 4 5 5l2-2 3 3-2 3C7 15 1 9 1 3z" fill="var(--blue)"/></svg><span>123 456 7890</span></div>
<div class="contact" style="top:3309px"><svg width="16" height="14" viewBox="0 0 16 14"><rect x="1" y="1" width="14" height="12" rx="1" fill="none" stroke="var(--blue)" stroke-width="1.6"/><path d="M1 2l7 6 7-6" fill="none" stroke="var(--blue)" stroke-width="1.6"/></svg><span>info@kremedical.com</span></div>
<div class="contact" style="top:3350px"><svg width="16" height="16" viewBox="0 0 16 16" fill="none" stroke="var(--blue)" stroke-width="1.4"><circle cx="8" cy="8" r="7"/><ellipse cx="8" cy="8" rx="3" ry="7"/><line x1="1" y1="8" x2="15" y2="8"/></svg><span>www.kremedical.com</span></div>

<div class="abs copy">© KRE MEDICAL - 2017. All Rights Reserved.</div>

</body>
</html>
```